Corvex Power is after a design for our corporate business cards. We work in the electricity industry and our corporate colours are those shown in the Logo (attached). We are looking for something professional that incorporates our colours (although don't want the colours to dominate at the same time). These can be double sided, logo on rear and personal information for our staff on the front side. Our industry is a dangerous one, so we promote safety through our vision statement of "Safety Never Takes a Day Off" this can be incorporated on the card somewhere also.

```html
<!DOCTYPE html>
<html lang="en">
<head>
<meta charset="utf-8">
<title>Corvex Power – Business Cards</title>
<link href="https://fonts.googleapis.com/css2?family=Montserrat:wght@500;600;700&family=Open+Sans:wght@400;600&display=swap" rel="stylesheet">
<style>
  :root{
    --backdrop:#e4e4e2;
    --card-white:#ffffff;
    --card-grey:#9c9c9c;
    --brand-green:#6cb33f;
    --brand-grey:#8c8c8c;
    --ink-dark:#3a3a3a;
    --ink-mid:#7a7a7a;
    --silver:#d9d9d9;
  }
  *{margin:0;padding:0;box-sizing:border-box}
  html,body{width:1200px;height:715px;overflow:hidden}
  body{background:var(--backdrop);position:relative;font-family:'Open Sans',Arial,sans-serif}
  .card{position:absolute;width:500px;height:286px;border-radius:3px;box-shadow:0 6px 18px rgba(0,0,0,.18)}
  .card--front{left:70px;top:215px;background:var(--card-white)}
  .card--back{left:630px;top:215px;background:var(--card-grey)}

  .wordmark{position:absolute;display:flex;align-items:center;gap:8px;font-family:'Montserrat',Arial,sans-serif;font-weight:700;letter-spacing:.5px;white-space:nowrap}
  .wordmark__dot{border-radius:50%;flex:none}
  .card--front .wordmark{left:30px;top:40px;font-size:15px;color:var(--brand-grey)}
  .card--front .wordmark__dot{width:22px;height:22px;background:var(--brand-green)}
  .card--back .wordmark{left:0;right:0;top:122px;justify-content:center;font-size:32px;color:var(--silver)}
  .card--back .wordmark__dot{width:34px;height:34px;background:var(--silver)}

  .person{position:absolute;left:260px;top:38px}
  .person__name{font-family:'Montserrat',Arial,sans-serif;font-weight:700;font-size:17px;color:var(--ink-dark)}
  .person__role{font-family:'Montserrat',Arial,sans-serif;font-weight:600;font-size:11px;letter-spacing:.5px;color:var(--brand-green);margin-top:2px}
  .person__rule{width:110px;height:2px;background:var(--brand-green);margin-top:6px}

  .contact{position:absolute;left:260px;top:100px;font-size:11.5px;line-height:19px;color:var(--brand-green);white-space:nowrap}
  .contact__value{color:var(--ink-mid)}
  .website{position:absolute;left:30px;top:150px;font-size:12px;font-weight:600;color:var(--brand-green);letter-spacing:.3px}
</style>
</head>
<body>
  <section class="card card--front" aria-label="Business card front">
    <div class="wordmark"><span class="wordmark__dot"></span>CORVEX POWER</div>
    <div class="person">
      <div class="person__name">Owen Hale</div>
      <div class="person__role">CO-FOUNDER</div>
      <div class="person__rule"></div>
    </div>
    <div class="contact">
      <div>212-218 Harbour Road West</div>
      <div>Ashford, Ontario K4R 2M6</div>
      <div>Phone: <span class="contact__value">(555) 240-7316</span></div>
      <div>Mobile: <span class="contact__value">(555) 240-7316</span></div>
      <div>Email: <span class="contact__value">owen@corvexpower.com</span></div>
    </div>
    <div class="website">www.corvexpower.com</div>
  </section>

  <section class="card card--back" aria-label="Business card back">
    <div class="wordmark"><span class="wordmark__dot"></span>CORVEX POWER</div>
  </section>
</body>
</html>
```